Im open to ideas.. I was thinking on my business cards aswell as my logo. a place for my name. email. phone number and abn..

ive attched a file with my business logo. which i dont love the colours.. i was think a dark background with charcoal letters so something along those colour schumes but im open to ideas..

Business

BRL Constructions

```html
<!DOCTYPE html>
<html lang="en">
<head>
<meta charset="utf-8">
<title>BRL Constructions – Business Card</title>
<link href="https://fonts.googleapis.com/css2?family=Roboto:wght@400;500;700&display=swap" rel="stylesheet">
<style>
  :root {
    --backdrop: #2b2b2c;
    --charcoal: #3b3c3e;
    --charcoal-deep: #303133;
    --accent-red: #e0121b;
    --card-white: #f4f4f4;
    --card-shade: #dcdcdc;
    --text-dark: #333438;
    --text-mid: #4a4b4f;
  }
  * { margin: 0; padding: 0; box-sizing: border-box; }
  html, body {
    width: 1200px;
    height: 997px;
    overflow: hidden;
    background: var(--backdrop);
    font-family: "Roboto", Arial, sans-serif;
  }
  .business-card {
    position: absolute;
    left: 180px;
    top: 258px;
    width: 840px;
    height: 480px;
    border-radius: 22px;
    overflow: hidden;
    background: linear-gradient(160deg, var(--card-white) 40%, var(--card-shade) 100%);
    box-shadow: 0 18px 40px rgba(0,0,0,0.45);
  }
  .header-band {
    position: absolute;
    left: 0;
    top: 0;
    width: 100%;
    height: 150px;
    background: linear-gradient(180deg, var(--charcoal) 0%, var(--charcoal-deep) 100%);
  }
  .accent-stripe {
    position: absolute;
    left: 0;
    top: 150px;
    width: 100%;
    height: 14px;
    background: var(--accent-red);
  }
  .brand-name {
    position: absolute;
    right: 56px;
    top: 206px;
    display: flex;
    align-items: center;
    gap: 12px;
    font-size: 40px;
    font-weight: 700;
    color: var(--text-dark);
    letter-spacing: 0.5px;
    line-height: 1;
  }
  .brand-mark {
    width: 18px;
    height: 18px;
    background: var(--accent-red);
  }
  .contact-block {
    position: absolute;
    left: 50px;
    top: 262px;
  }
  .person-name {
    font-size: 26px;
    font-weight: 500;
    color: var(--accent-red);
    line-height: 1.1;
  }
  .person-title {
    font-size: 16px;
    color: var(--text-mid);
    margin-bottom: 22px;
  }
  .contact-line {
    display: flex;
    align-items: center;
    gap: 14px;
    font-size: 19px;
    line-height: 1.3;
    color: var(--text-mid);
    margin-bottom: 6px;
  }
  .contact-icon { width: 16px; height: 16px; flex: none; }
  .abn-label {
    width: 16px;
    flex: none;
    font-size: 10px;
    font-weight: 700;
    color: var(--accent-red);
  }
  .web-address {
    margin-left: 30px;
    font-size: 20px;
    font-weight: 700;
    color: var(--accent-red);
  }
</style>
</head>
<body>
  <div class="business-card">
    <div class="header-band" role="img" aria-label="Charcoal header area with a red house roofline illustration"></div>
    <div class="accent-stripe"></div>

    <div class="brand-name"><span class="brand-mark"></span>BRL Constructions</div>

    <div class="contact-block">
      <p class="person-name">Daniel Morrow</p>
      <p class="person-title">CEO &amp; Managing Director</p>
      <p class="contact-line">
        <svg class="contact-icon" viewBox="0 0 16 16" aria-hidden="true"><path d="M3 1h3l1.5 4-2 1.2a8 8 0 0 0 4.3 4.3L11 8.5l4 1.5v3a2 2 0 0 1-2 2A12 12 0 0 1 1 3a2 2 0 0 1 2-2z" fill="var(--accent-red)"/></svg>
        0400 123 456
      </p>
      <p class="contact-line">
        <svg class="contact-icon" viewBox="0 0 16 16" aria-hidden="true"><rect x="1" y="3" width="14" height="10" fill="var(--accent-red)"/><polyline points="1,3 8,9 15,3" fill="none" stroke="#fff" stroke-width="1.4"/></svg>
        info@brlconstructions.com
      </p>
      <p class="contact-line">
        <span class="abn-label">ABN</span>
        12 345 678 901
      </p>
      <p class="web-address">www.brlconstructions.com</p>
    </div>
  </div>
</body>
</html>
```